Need Help having my business card stand out

I am the owner of Pine Ridge Canine Coaching and would like for my business cards to stand out. I have been trying to keep designing them myself but I can't get what I have in my head on the card. I will try my best to post templates that I like for inspirations. I want something unique but elegant. I don't want in to look cartoony or cheesy. It needs to pop in a pet shop but also in a coffee shop or gym.

Target Market(s)

Dog owners, Married ,No young kids Jr High school kids and up (maybe kids on the way) Executives, Stay at home moms/wives, Small business owners

Industry/Entity Type

Dog Training

Contact Information for Business Card

Trevor Holloway, 555-304-7162, info@pineridgecanine.example, www.pineridgecanine.example

Colors

Designer to choose colors to be used in the design.

Requirements
Must have
• my logo
Should not have
• Cursive lettering

```html
<!DOCTYPE html>
<html lang="en">
<head>
<meta charset="utf-8">
<title>Pine Ridge Canine Coaching – Business Card</title>
<link href="https://fonts.googleapis.com/css2?family=Inter:wght@300;400;500;600&display=swap" rel="stylesheet">
<style>
  :root {
    --backdrop: #2b2b2e;
    --card-white: #f4f4f4;
    --ink-dark: #1e2326;
    --ink-mid: #3a3d40;
    --ink-soft: #6b6e71;
    --rule: #2a2d30;
    --ghost-light: #f1f1f1;
    --ghost-deep: #e8e8e8;
  }
  * { box-sizing: border-box; margin: 0; padding: 0; }
  html, body {
    width: 1200px; height: 900px; overflow: hidden;
    background: var(--backdrop);
    font-family: "Inter", Arial, sans-serif;
  }
  .canvas { position: relative; width: 1200px; height: 900px; }
  .card {
    position: absolute; left: 290px;
    width: 620px; height: 354px;
    border-radius: 26px; overflow: hidden;
    background: var(--card-white);
    box-shadow: 0 10px 30px rgba(0,0,0,.35);
  }
  .card--front { top: 66px; }
  .card--back { top: 480px; }
  .card svg { position: absolute; inset: 0; }

  .badge {
    position: absolute; left: 286px; top: 66px;
    width: 208px; height: 208px; border-radius: 50%;
    display: flex; align-items: center; justify-content: center;
    text-align: center;
  }
  .badge-name {
    font-weight: 600; font-size: 22px; line-height: 1.3;
    color: var(--ink-dark); letter-spacing: .02em;
  }

  .back-content {
    position: absolute; inset: 0;
    display: flex; flex-direction: column; align-items: center;
    padding-top: 34px; text-align: center; color: var(--ink-dark);
  }
  .brand-name {
    font-weight: 600; font-size: 24px; color: var(--ink-dark);
    letter-spacing: .02em; margin-bottom: 22px;
  }
  .person-name {
    font-weight: 400; font-size: 22px; letter-spacing: .04em;
    color: var(--ink-mid); text-transform: uppercase;
  }
  .person-role { font-weight: 300; font-size: 15px; color: var(--ink-soft); margin-top: 2px; }
  .divider { width: 60px; height: 1.5px; background: var(--rule); margin: 14px 0; }
  .contact-list { list-style: none; font-size: 15px; line-height: 1.6; color: var(--ink-mid); }
  .contact-list .address { font-weight: 500; color: var(--ink-dark); }
  .watermark-art {
    position: absolute; right: 40px; bottom: 0;
    width: 190px; height: 88px;
    border-radius: 60px 60px 0 0;
    background: linear-gradient(180deg, var(--ghost-light) 0%, var(--ghost-deep) 100%);
  }
</style>
</head>
<body>
<main class="canvas">

  <section class="card card--front" aria-label="Card front">
    <svg width="620" height="354" viewBox="0 0 620 354" aria-hidden="true">
      <polygon points="200,354 340,354 480,0 340,0" fill="#1e2326"/>
      <polygon points="225,354 240,354 380,0 365,0" fill="#f4f4f4"/>
      <polygon points="355,354 405,354 545,0 495,0" fill="#1e2326"/>
      <polygon points="160,354 172,354 312,0 300,0" fill="#1e2326"/>
      <circle cx="390" cy="170" r="116" fill="#f4f4f4" stroke="#1e2326" stroke-width="24"/>
    </svg>
    <div class="badge"><div class="badge-name">Pine Ridge<br>Canine Coaching</div></div>
  </section>

  <section class="card card--back" aria-label="Card back">
    <div class="watermark-art" role="img" aria-label="Faint dog illustration watermark"></div>
    <div class="back-content">
      <div class="brand-name">Pine Ridge Canine Coaching</div>
      <div class="person-name">Trevor Holloway</div>
      <div class="person-role">General Manager</div>
      <div class="divider"></div>
      <ul class="contact-list">
        <li>555-304-7162</li>
        <li>info@pineridgecanine.example</li>
        <li>pineridgecanine.example</li>
        <li class="address">Pine Ridge Canine Coaching, 55501 Cedar Hollow, United States</li>
      </ul>
    </div>
  </section>

</main>
</body>
</html>
```